Harlow Capital - Financial Planning Solutions

Harlow Capital is a financial planning business in Melbourne, Australia. We cater to all kinds of clients from high net worth individuals to young people just starting a career. We need a chart, which will be included in client pitches, presentations and on our website, that conveys the various areas that we are able to provide client solutions.
We have attached three rudimentary interpretations of what we're talking about, one of which includes our logo. With each area of advice we have included a brief description of what it is. The different areas are not necessarily linked, so it's not a circular process but there is a logical progression to them: clients can ask us to get involved with any of the steps.
We are pretty open to suggestions as to the best presentation but are quite interested in an infographics approach.
You can check out our website at www.harlowcapital.com.au to see a bit about us, but please be aware that we are changing our investment philosophy and the tone of the website to a broader appeal.
Cheers, Oliver

Industry/Entity Type

Investment

```html
<!DOCTYPE html>
<html lang="en">
<head>
<meta charset="utf-8">
<title>Harlow Capital – Client Solutions</title>
<link rel="stylesheet" href="https://fonts.googleapis.com/css2?family=Montserrat:wght@300;400&family=Roboto+Condensed:wght@400&family=Tinos&display=swap">
<style>
  :root {
    --canvas-bg: #e6e7e8;
    --ink: #060606;
    --tan: #a69a74;
    --white: #ffffff;
    --col-width: 121px;
    --base-line: 871px;
  }
  * { margin: 0; padding: 0; box-sizing: border-box; }
  html, body { width: 1200px; height: 927px; overflow: hidden; background: var(--canvas-bg); }
  .chart {
    position: relative;
    width: 1200px;
    height: 927px;
    background: var(--canvas-bg);
  }
  .chart-title {
    position: absolute;
    left: 30px;
    top: 62px;
    font-family: "Montserrat", sans-serif;
    font-weight: 300;
    font-size: 40px;
    letter-spacing: 4px;
    color: var(--ink);
  }
  .brand {
    position: absolute;
    right: 32px;
    top: 56px;
    display: flex;
    align-items: center;
    gap: 12px;
  }
  .brand-mark {
    width: 26px;
    height: 26px;
    background: var(--ink);
  }
  .brand-name {
    font-family: "Montserrat", sans-serif;
    font-weight: 400;
    font-size: 26px;
    letter-spacing: 3px;
    color: var(--ink);
    text-transform: uppercase;
  }
  .step {
    position: absolute;
    top: var(--top);
    left: var(--left);
    width: var(--col-width);
    height: calc(var(--base-line) - var(--top));
    display: flex;
    flex-direction: column;
  }
  .step-label {
    height: 50px;
    background: var(--tan);
    color: var(--white);
    font-family: "Roboto Condensed", sans-serif;
    font-size: 14.5px;
    line-height: 1.1;
    text-transform: uppercase;
    letter-spacing: 0.3px;
    display: flex;
    align-items: center;
    justify-content: center;
    text-align: center;
    padding: 0 4px;
  }
  .step-label.small { font-size: 12.5px; }
  .step-body {
    position: relative;
    flex: 1;
    background: var(--ink);
    clip-path: polygon(0 0, 100% 0, 100% 100%, 50% calc(100% - 34px), 0 100%);
  }
  .step-text {
    position: absolute;
    top: calc(656px - var(--top) - 50px);
    left: 12px;
    right: 8px;
    font-family: "Tinos", serif;
    font-size: 13.5px;
    line-height: 1.55;
    color: var(--white);
  }
</style>
</head>
<body>
<main class="chart">
  <h1 class="chart-title">CLIENT SOLUTIONS</h1>

  <div class="brand">
    <span class="brand-mark"></span>
    <span class="brand-name">Harlow Capital</span>
  </div>

  <section class="step" style="--left:30px; --top:548px;">
    <div class="step-label">Household<br>Income</div>
    <div class="step-body"><p class="step-text">Funds<br>earned from<br>work or<br>investments</p></div>
  </section>

  <section class="step" style="--left:178px; --top:492px;">
    <div class="step-label">Tax Advice</div>
    <div class="step-body"><p class="step-text">Maximise after<br>tax income</p></div>
  </section>

  <section class="step" style="--left:326px; --top:442px;">
    <div class="step-label">Financial<br>Planning</div>
    <div class="step-body"><p class="step-text">A road map for<br>the application<br>of your after<br>tax income</p></div>
  </section>

  <section class="step" style="--left:474px; --top:391px;">
    <div class="step-label">Debt</div>
    <div class="step-body"><p class="step-text">To fund the<br>purchase of a<br>house or<br>other asset</p></div>
  </section>

  <section class="step" style="--left:621px; --top:342px;">
    <div class="step-label">Super<br>Annuation</div>
    <div class="step-body"><p class="step-text">Advice on<br>structuring and<br>management</p></div>
  </section>

  <section class="step" style="--left:762px; --top:291px;">
    <div class="step-label">Investment<br>Portfolio</div>
    <div class="step-body"><p class="step-text">Optimise the<br>return on your<br>after tax<br>income</p></div>
  </section>

  <section class="step" style="--left:909px; --top:230px;">
    <div class="step-label small">Insurance &amp;<br>Risk Protection</div>
    <div class="step-body"><p class="step-text">Protect the<br>lifestyle<br>you’ve built<br>for you and<br>your family</p></div>
  </section>

  <section class="step" style="--left:1057px; --top:179px;">
    <div class="step-label">Estate<br>Planning</div>
    <div class="step-body"><p class="step-text">Ensure your<br>assests are<br>dealt with as<br>you want</p></div>
  </section>
</main>
</body>
</html>
```